Author and Publisher

Cover for a book on the process of publishing a book from the presentation to the publisher until the selling in bookstores :
A behind-the-scenes journey through the world of book publishing, from manuscript to bookstore. The book explores the relationship between authors and publishers, manuscript selection, contracts, editing, proofreading, book design, printing, distribution, bookstores and online sales. It reveals the many people, decisions and processes involved in turning a text into a physical book and bringing it to readers. The illustration should evoke publishing as a lively, contemporary ecosystem, combining creativity, craftsmanship, business and the enduring appeal of books.
FORMAT : 14 x 20,5 cm
AUTHOR : Luc Varennes
TITLE : Le scribe et la presse
PUBLISHER : Editions Trovel (at the bottom of the page)
Target Market(s)
General public, mainly news authors of books
Look and feel
Each slider illustrates characteristics of the customer's brand and the style your logo design should communicate.

```html
<!DOCTYPE html>
<html lang="fr">
<head>
<meta charset="utf-8">
<title>Le scribe et la presse — Luc Varennes</title>
<link rel="stylesheet" href="https://fonts.googleapis.com/css2?family=Inter:wght@600;700&family=Playfair+Display:wght@700&display=swap">
<style>
  :root {
    --paper: #f1e4d3;
    --paper-light: #f5ebdd;
    --ink: #1c2137;
    --rust: #b0401a;
    --white: #ffffff;
    --gap: #e9dccb;
  }
  * { margin: 0; padding: 0; box-sizing: border-box; }
  html, body { width: 820px; height: 1200px; overflow: hidden; }
  body { background: var(--paper); }
  .cover {
    position: relative;
    width: 820px;
    height: 1200px;
    overflow: hidden;
    background: linear-gradient(to bottom, var(--paper-light) 0%, #f2e6d6 50%, #ecdcc8 62%);
  }
  .bookshelf-photo {
    position: absolute;
    left: 0;
    top: 640px;
    width: 820px;
    height: 560px;
    background:
      radial-gradient(ellipse 260px 120px at 90px 330px, rgba(246, 214, 178, 0.9) 0%, rgba(246, 214, 178, 0) 100%),
      radial-gradient(ellipse 230px 300px at 720px 330px, rgba(150, 150, 158, 0.75) 0%, rgba(150, 150, 158, 0) 100%),
      radial-gradient(ellipse 260px 260px at 430px 330px, rgba(120, 58, 52, 0.55) 0%, rgba(120, 58, 52, 0) 100%),
      radial-gradient(ellipse 200px 80px at 180px 440px, rgba(232, 228, 220, 0.8) 0%, rgba(232, 228, 220, 0) 100%),
      linear-gradient(to bottom, rgba(236, 220, 200, 0) 0%, #e7cdb4 28%, #c9a089 48%, #9a7274 66%, #6a5262 82%, #3d3145 100%);
  }
  .author {
    position: absolute;
    top: 56px;
    left: 0;
    width: 100%;
    text-align: center;
    font-family: "Inter", sans-serif;
    font-weight: 600;
    font-size: 36px;
    color: var(--ink);
  }
  .author-rule {
    position: absolute;
    top: 108px;
    left: 383px;
    width: 54px;
    height: 3px;
    background: var(--rust);
  }
  .title {
    position: absolute;
    top: 110px;
    left: 0;
    width: 100%;
    text-align: center;
    font-family: "Playfair Display", serif;
    font-weight: 700;
    color: var(--ink);
    font-size: 122px;
    line-height: 134px;
    letter-spacing: -1px;
  }
  .title-line { display: block; white-space: nowrap; }
  .title-accent { color: var(--rust); }
  .mosaic {
    position: absolute;
    left: 0;
    top: 0;
    width: 820px;
    height: 1200px;
  }
  .publisher {
    position: absolute;
    bottom: 26px;
    left: 0;
    width: 100%;
    text-align: center;
    font-family: "Inter", sans-serif;
    font-weight: 600;
    font-size: 27px;
    color: var(--white);
  }
  .series-code {
    position: absolute;
    bottom: 24px;
    right: 20px;
    font-family: "Inter", sans-serif;
    font-weight: 700;
    font-size: 17px;
    color: var(--white);
  }
</style>
</head>
<body>
  <main class="cover">
    <div class="bookshelf-photo" role="img" aria-label="Photographie de livres debout, de piles de volumes et d'un magazine ouvert sur une table reflétante, dans une lumière de fin de journée"></div>

    <p class="author">Luc Varennes</p>
    <div class="author-rule"></div>

    <h1 class="title">
      <span class="title-line">Le scribe</span>
      <span class="title-line"><span class="title-accent">et</span> la presse</span>
    </h1>

    <svg class="mosaic" viewBox="0 0 820 1200" width="820" height="1200">
      <defs>
        <linearGradient id="tile-desk" x1="0" y1="0" x2="0.3" y2="1">
          <stop offset="0" stop-color="#7a3e25"/>
          <stop offset="0.3" stop-color="#5a3a2c"/>
          <stop offset="0.5" stop-color="#cfc6b8"/>
          <stop offset="0.68" stop-color="#2e2b2c"/>
          <stop offset="0.85" stop-color="#e4dccd"/>
          <stop offset="1" stop-color="#cbbca2"/>
        </linearGradient>
        <linearGradient id="tile-hand" x1="0" y1="0" x2="1" y2="1">
          <stop offset="0" stop-color="#d7c3a2"/>
          <stop offset="0.35" stop-color="#d9a67e"/>
          <stop offset="0.55" stop-color="#e8d6c0"/>
          <stop offset="1" stop-color="#f2ede6"/>
        </linearGradient>
        <linearGradient id="tile-library" x1="0" y1="0" x2="1" y2="0.4">
          <stop offset="0" stop-color="#1f1f1f"/>
          <stop offset="0.35" stop-color="#5c5c5c"/>
          <stop offset="0.6" stop-color="#9a9a9a"/>
          <stop offset="0.8" stop-color="#4a4a4a"/>
          <stop offset="1" stop-color="#1a1a1a"/>
        </linearGradient>
        <linearGradient id="tile-books" x1="0" y1="0" x2="0" y2="1">
          <stop offset="0" stop-color="#6b4a33"/>
          <stop offset="0.3" stop-color="#e6d8bd"/>
          <stop offset="0.55" stop-color="#2f3f5e"/>
          <stop offset="0.68" stop-color="#6e2a25"/>
          <stop offset="0.8" stop-color="#2e4f3c"/>
          <stop offset="1" stop-color="#8a5a35"/>
        </linearGradient>
      </defs>
      <polygon points="416,395 540,507 416,619 292,507" fill="url(#tile-desk)" role="img" aria-label="Ordinateur portable et manuscrit ouvert sur un bureau devant une bibliothèque"/>
      <polygon points="286,512 408,623 286,734 164,623" fill="url(#tile-hand)" role="img" aria-label="Main écrivant au stylo sur une feuille blanche"/>
      <polygon points="538,517 663,627 538,737 413,627" fill="url(#tile-library)" role="img" aria-label="Photographie en noir et blanc d'un lecteur dans les rayonnages d'une bibliothèque"/>
      <polygon points="411,633 535,744 411,855 287,744" fill="url(#tile-books)" role="img" aria-label="Livre ancien ouvert posé sur une pile de trois volumes reliés bleu, rouge et vert"/>
    </svg>

    <p class="publisher">Editions Trovel</p>
    <p class="series-code">C56</p>
  </main>
</body>
</html>
```